BrivaTrek Freight Services Business cards

Would like a very unique design catchy but professional for business cards. Please use log provided.Marlon WellsCeo and Founder TransCon Logistix Solutions1-888-913-3225mwells@tlsolutionsus.comwww.bfservicesco.com

```html
<!DOCTYPE html>
<html lang="en">
<head>
<meta charset="utf-8">
<title>BrivaTrek Freight Services – Business Card</title>
<link rel="stylesheet" href="https://fonts.googleapis.com/css2?family=Ubuntu:wght@400;500&display=swap">
<style>
  :root {
    --page: #e8e5e0;
    --card: #f5f4f2;
    --navy: #1f3f7a;
    --red: #c0171f;
    --band-blue: #2b5a92;
    --band-red: #c0141c;
  }
  * { box-sizing: border-box; margin: 0; padding: 0; }
  html, body { width: 1200px; height: 970px; overflow: hidden; }
  body {
    background: var(--page);
    font-family: "Ubuntu", sans-serif;
    position: relative;
  }
  .card {
    position: absolute;
    left: 80px; top: 188px;
    width: 1040px; height: 594px;
    background: var(--card);
    box-shadow: 0 10px 30px rgba(0,0,0,0.12);
  }
  .brand-name {
    position: absolute;
    left: 0; right: 0; top: 208px;
    text-align: center;
    color: var(--navy);
    font-size: 40px;
    font-weight: 500;
    letter-spacing: 0.5px;
  }
  .holder-name {
    position: absolute;
    left: 0; right: 0; top: 376px;
    text-align: center;
    color: var(--navy);
    font-size: 35px;
    font-weight: 400;
  }
  .title-row {
    position: absolute;
    left: 55px; right: 62px; top: 410px;
    display: flex; align-items: center; gap: 10px;
  }
  .title-row .rule { flex: 1; height: 2px; background: var(--red); }
  .holder-title { color: var(--red); font-size: 25px; line-height: 30px; }
  .contact {
    position: absolute; left: 52px; top: 470px;
    display: flex; flex-direction: column; gap: 6px;
  }
  .contact-item {
    display: flex; align-items: center; gap: 8px;
    color: var(--navy); font-size: 26px; line-height: 28px;
  }
  .contact-item svg { width: 30px; height: 30px; flex: none; }
  .company-block {
    position: absolute; right: 62px; top: 468px;
    text-align: right; display: flex; flex-direction: column; gap: 4px;
  }
  .company-line { color: var(--red); font-size: 26px; line-height: 30px; }
  .web-line { color: var(--navy); font-size: 26px; line-height: 30px; }
  .band {
    position: absolute; left: 0; right: 0; bottom: 0; height: 18px;
    display: flex;
  }
  .band .blue { flex: 1; background: var(--band-blue); }
  .band .red { flex: 1; background: var(--band-red); }
</style>
</head>
<body>
  <section class="card">
    <div class="brand-name">BrivaTrek Freight Services</div>

    <div class="holder-name">Dustin Harrow</div>
    <div class="title-row">
      <span class="rule"></span>
      <span class="holder-title">Ceo and Founder</span>
      <span class="rule"></span>
    </div>

    <div class="contact">
      <div class="contact-item">
        <svg viewBox="0 0 30 30" aria-hidden="true">
          <circle cx="15" cy="15" r="13" fill="none" stroke="var(--red)" stroke-width="2.5"/>
          <circle cx="15" cy="15" r="9.5" fill="var(--red)"/>
          <rect x="11.5" y="9" width="7" height="12" rx="1.5" fill="none" stroke="#fff" stroke-width="1.6"/>
        </svg>
        <span>1-888-472-6081</span>
      </div>
      <div class="contact-item">
        <svg viewBox="0 0 30 30" aria-hidden="true">
          <circle cx="15" cy="15" r="13" fill="none" stroke="var(--red)" stroke-width="2.5"/>
          <circle cx="15" cy="15" r="9.5" fill="var(--red)"/>
          <rect x="9.5" y="11" width="11" height="8" fill="none" stroke="#fff" stroke-width="1.4"/>
          <polyline points="9.5,11 15,15.5 20.5,11" fill="none" stroke="#fff" stroke-width="1.4"/>
        </svg>
        <span>dharrow@bfservicesco.com</span>
      </div>
    </div>

    <div class="company-block">
      <span class="company-line">BrivaTrek Freight Services</span>
      <span class="web-line">www.bfservicesco.com</span>
    </div>

    <div class="band"><span class="blue"></span><span class="red"></span></div>
  </section>
</body>
</html>
```